Borrowdale Equity Business Card

Looking for a design for our business cards. Need to look corporate and outstanding. I have enclosed our logos for the company. Borrowdale equity is an investment firm for high level clients looking for advisory in their investments. White background or black is good. We will like to double sided options maybe at the back with just the logo of the firm.

Example of the info for the business card:

Marcus Heller
Managing Director

Panama Phone +507 391 4786
Switzerland Phone +41 43 917 2648
test@borrowdale-equity-example.com
www.borrowdale-equity-example.com

Industry/Entity Type

Investment

```html
<!DOCTYPE html>
<html lang="en">
<head>
<meta charset="utf-8">
<title>Borrowdale Equity Business Card</title>
<link href="https://fonts.googleapis.com/css2?family=Open+Sans:wght@400;600&display=swap" rel="stylesheet">
<style>
  :root {
    --backdrop: #e9e6e1;
    --card-black: #111317;
    --card-black-soft: #1c1f25;
    --card-white: #ffffff;
    --navy: #2b3f8c;
    --gold: #b8902f;
    --name-blue: #3f63c6;
    --text-light: #f2f2f2;
    --text-muted: #d6d6d6;
  }
  * { box-sizing: border-box; margin: 0; padding: 0; }
  html, body {
    width: 1200px;
    height: 784px;
    overflow: hidden;
    background: var(--backdrop);
    font-family: "Open Sans", Arial, sans-serif;
  }
  .canvas {
    position: relative;
    width: 1200px;
    height: 784px;
  }
  .card {
    position: absolute;
    width: 560px;
    height: 320px;
    border-radius: 4px;
    overflow: hidden;
    box-shadow: 0 8px 22px rgba(0,0,0,0.22);
  }
  .wordmark {
    display: flex;
    align-items: center;
    gap: 14px;
    font-weight: 600;
    color: var(--navy);
    letter-spacing: 0.5px;
    white-space: nowrap;
  }
  .wordmark-square {
    width: 30px;
    height: 30px;
    background: var(--navy);
    flex: none;
  }

  /* Back side */
  .card-back {
    left: 60px;
    top: 50px;
    background: radial-gradient(ellipse at 40% 35%, var(--card-black-soft), var(--card-black) 75%);
    display: flex;
    align-items: center;
    justify-content: center;
  }
  .card-back .wordmark { font-size: 30px; }

  /* Front side */
  .card-front {
    left: 580px;
    top: 414px;
    background: var(--card-black);
  }
  .front-top {
    height: 140px;
    background: var(--card-white);
    display: flex;
    align-items: center;
    padding-left: 44px;
  }
  .front-top .wordmark { font-size: 30px; }
  .front-divider {
    height: 7px;
    background: var(--gold);
  }
  .front-bottom {
    height: 173px;
    background: radial-gradient(ellipse at 60% 30%, var(--card-black-soft), var(--card-black) 80%);
    padding: 18px 0 0 30px;
    color: var(--text-light);
  }
  .holder-name {
    font-size: 17px;
    font-weight: 400;
    color: var(--name-blue);
    line-height: 1.2;
  }
  .holder-title {
    font-size: 10.5px;
    font-weight: 600;
    color: var(--text-muted);
    margin-bottom: 20px;
  }
  .contact-list {
    list-style: none;
    font-size: 13.5px;
    line-height: 1.4;
  }
</style>
</head>
<body>
  <main class="canvas">
    <section class="card card-back" aria-label="Card back">
      <div class="wordmark"><span class="wordmark-square"></span>Borrowdale Equity</div>
    </section>

    <section class="card card-front" aria-label="Card front">
      <div class="front-top">
        <div class="wordmark"><span class="wordmark-square"></span>Borrowdale Equity</div>
      </div>
      <div class="front-divider"></div>
      <div class="front-bottom">
        <p class="holder-name">Marcus Heller</p>
        <p class="holder-title">Managing Director</p>
        <ul class="contact-list">
          <li>Panama Phone +507 391 4786</li>
          <li>Switzerland Phone +41 43 917 2648</li>
          <li>test@borrowdale-equity-example.com</li>
          <li>www.borrowdale-equity-example.com</li>
        </ul>
      </div>
    </section>
  </main>
</body>
</html>
```